Now Leasing Banner

Looking for a banner that says the following information approx 4' x 30'

Now Leasing Maple Ridge Court 925-318-6042

Target Market(s)

Drive by traffic

Industry/Entity Type

Residential property management

Requirements
Must have
• Clear and readable from a distance

```html
<!DOCTYPE html>
<html lang="en">
<head>
<meta charset="utf-8">
<title>Now Leasing Banner – Maple Ridge Court</title>
<link href="https://fonts.googleapis.com/css2?family=Anton&display=swap" rel="stylesheet">
<style>
  :root {
    --page-bg: #e9eaec;
    --banner-black: #141414;
    --banner-yellow: #f3c51c;
    --rule-white: #ffffff;
    --letter-outline: #ffffff;
    --letter-shadow: #111111;
  }
  html, body {
    margin: 0;
    padding: 0;
    width: 1200px;
    height: 800px;
    overflow: hidden;
    background: var(--page-bg);
  }
  .canvas {
    position: relative;
    width: 1200px;
    height: 800px;
    display: flex;
    align-items: center;
    justify-content: center;
  }
  .banner {
    display: block;
    width: 1160px;
    height: 155px;
  }
  .banner-frame { fill: var(--banner-black); }
  .banner-field { fill: var(--banner-yellow); }
  .banner-rule { fill: var(--rule-white); }
  .headline {
    font-family: "Anton", "Impact", sans-serif;
    font-size: 64px;
    letter-spacing: 1px;
  }
  .headline-outline {
    fill: var(--letter-outline);
    stroke: var(--letter-outline);
    stroke-width: 12;
    stroke-linejoin: round;
  }
  .headline-shadow {
    fill: var(--letter-shadow);
    stroke: var(--letter-shadow);
    stroke-width: 4;
    stroke-linejoin: round;
  }
  .headline-face {
    fill: var(--banner-yellow);
    stroke: var(--letter-shadow);
    stroke-width: 2.5;
    stroke-linejoin: round;
    paint-order: stroke fill;
  }
</style>
</head>
<body>
  <main class="canvas">
    <svg class="banner" viewBox="0 0 1160 155" role="img" aria-label="Now Leasing Maple Ridge Court 925-318-6042">
      <rect class="banner-frame" x="0" y="0" width="1160" height="155"/>
      <rect class="banner-rule" x="0" y="24" width="1160" height="3"/>
      <rect class="banner-field" x="0" y="27" width="1160" height="101"/>
      <rect class="banner-rule" x="0" y="128" width="1160" height="3"/>

      <g class="headline">
        <text class="headline-outline" x="32" y="102" textLength="1090" lengthAdjust="spacingAndGlyphs">NOW LEASING MAPLE RIDGE COURT 925-318-6042</text>
        <text class="headline-outline" x="37" y="107" textLength="1090" lengthAdjust="spacingAndGlyphs">NOW LEASING MAPLE RIDGE COURT 925-318-6042</text>
        <text class="headline-shadow" x="37" y="107" textLength="1090" lengthAdjust="spacingAndGlyphs">NOW LEASING MAPLE RIDGE COURT 925-318-6042</text>
        <text class="headline-face" x="32" y="102" textLength="1090" lengthAdjust="spacingAndGlyphs">NOW LEASING MAPLE RIDGE COURT 925-318-6042</text>
      </g>
    </svg>
  </main>
</body>
</html>
```